Cards for Employees

We are looking for an Anniversary and a Birthday card to send to our employees. 2 designs.
We send these cards to our employees based on number of years they work at the company.
Check out our website for more info.
www.BrightfoldServices.example
Target Market(s)
Our Employees -
Font styles to use
Sans Serif
Colors
Designer to choose colors to be used in the design.
Requirements
Must have
- Anniversary card - appreciation for hard work and dedication
Logo - no changes

```html
<!DOCTYPE html>
<html lang="en">
<head>
<meta charset="utf-8">
<title>Employee Cards – Brightfold Services</title>
<link href="https://fonts.googleapis.com/css2?family=Lato:wght@400;700;900&family=Pacifico&family=Michroma&family=Libre+Caslon+Text&display=swap" rel="stylesheet">
<style>
  :root {
    --backdrop: #454545;
    --birthday-blue: #2a6cbf;
    --birthday-glow: #3a86cc;
    --balloon: #8fa9e4;
    --anniv-top: #2b3f9c;
    --anniv-bottom: #1d2b78;
    --accent-red: #e3202a;
    --ink-white: #ffffff;
  }
  * { margin: 0; padding: 0; box-sizing: border-box; }
  html, body { width: 1200px; height: 1200px; overflow: hidden; }
  body { background: var(--backdrop); position: relative; font-family: "Lato", sans-serif; }

  .card { position: absolute; overflow: hidden; color: var(--ink-white); }

  /* Birthday card */
  .birthday-card {
    left: 74px; top: 63px; width: 667px; height: 518px;
    background: radial-gradient(ellipse at 50% 30%, var(--birthday-glow), var(--birthday-blue) 75%);
  }
  .balloons { position: absolute; }
  .balloons-top {
    left: 0; top: 0; width: 100%; height: 60px;
    background: linear-gradient(180deg, rgba(143,169,228,.75), rgba(143,169,228,0));
  }
  .balloons-right {
    left: 450px; top: 95px; width: 217px; height: 423px;
    background: radial-gradient(ellipse at 55% 50%, rgba(143,169,228,.75), rgba(143,169,228,0) 70%);
  }
  .balloons-left {
    left: -40px; top: 240px; width: 130px; height: 278px;
    background: radial-gradient(ellipse at 40% 60%, rgba(143,169,228,.75), rgba(143,169,228,0) 70%);
  }
  .greeting-intro { position: absolute; left: 74px; top: 122px; font-size: 22px; font-weight: 400; }
  .greeting-script {
    position: absolute; font-family: "Pacifico", cursive; font-size: 76px; line-height: 1;
    color: var(--ink-white);
  }
  .greeting-happy { left: 120px; top: 150px; }
  .greeting-birthday { left: 300px; top: 250px; }
  .divider { position: absolute; top: 385px; height: 3px; background: var(--ink-white); }
  .divider-left { left: 138px; width: 182px; }
  .divider-right { left: 356px; width: 182px; }
  .divider-dot { position: absolute; left: 331px; top: 379px; width: 15px; height: 15px; border-radius: 50%; background: var(--ink-white); }

  .company-name {
    position: absolute; text-align: center; font-family: "Lato", sans-serif; font-weight: 900;
    color: var(--ink-white); text-transform: uppercase; line-height: 1.05;
  }
  .birthday-card .company-name { left: 230px; top: 425px; width: 200px; font-size: 20px; }

  /* Anniversary card */
  .anniversary-card {
    left: 462px; top: 629px; width: 670px; height: 519px;
    background: linear-gradient(180deg, var(--anniv-top), var(--anniv-bottom));
  }
  .star-texture {
    position: absolute; inset: 0;
    background: radial-gradient(ellipse at 50% 20%, rgba(60,80,190,.45), rgba(60,80,190,0) 70%);
  }
  .anniversary-card .company-name { left: 170px; top: 90px; width: 336px; font-size: 30px; }
  .save-date {
    position: absolute; left: 0; width: 100%; top: 230px; text-align: center;
    font-family: "Michroma", sans-serif; font-size: 40px; letter-spacing: 2px;
  }
  .rule-red { position: absolute; height: 3px; background: var(--accent-red); }
  .rule-upper { left: 71px; top: 292px; width: 530px; }
  .rule-lower { left: 67px; top: 363px; width: 530px; }
  .occasion {
    position: absolute; left: 0; width: 100%; top: 308px; text-align: center;
    font-family: "Libre Caslon Text", serif; font-size: 30px; letter-spacing: .5px;
  }
  .date-frame { position: absolute; left: 74px; top: 442px; width: 520px; height: 100px; border: 1px solid rgba(255,255,255,.85); border-bottom: none; }
  .date-ribbon { position: absolute; left: 216px; top: 418px; }
  .date-text {
    position: absolute; left: 227px; top: 419px; width: 221px; height: 45px; line-height: 45px;
    text-align: center; font-family: "Libre Caslon Text", serif; font-size: 40px;
  }
</style>
</head>
<body>

<section class="card birthday-card">
  <div class="balloons balloons-top" role="img" aria-label="Row of light blue balloons along the top edge"></div>
  <div class="balloons balloons-right" role="img" aria-label="Cluster of light blue balloons on strings"></div>
  <div class="balloons balloons-left" role="img" aria-label="Light blue balloons at the left edge"></div>
  <p class="greeting-intro">We wish You</p>
  <p class="greeting-script greeting-happy">Happy</p>
  <p class="greeting-script greeting-birthday">Birthday</p>
  <div class="divider divider-left"></div>
  <div class="divider-dot"></div>
  <div class="divider divider-right"></div>
  <p class="company-name">Brightfold<br>Services</p>
</section>

<section class="card anniversary-card">
  <div class="star-texture" role="img" aria-label="Faint star pattern over a dark blue background"></div>
  <p class="company-name">Brightfold<br>Services</p>
  <h1 class="save-date">SAVE THE DATE</h1>
  <div class="rule-red rule-upper"></div>
  <p class="occasion">Celebrating Our 10th Anniversary</p>
  <div class="rule-red rule-lower"></div>
  <div class="date-frame"></div>
  <svg class="date-ribbon" width="244" height="48" viewBox="0 0 244 48" aria-hidden="true">
    <polygon points="0,0 14,0 14,46 0,46 9,23" fill="none" stroke="#ffffff" stroke-width="1"/>
    <polygon points="244,0 230,0 230,46 244,46 235,23" fill="none" stroke="#ffffff" stroke-width="1"/>
    <polygon points="4,1 240,1 231,24 240,46 4,46 13,24" fill="var(--accent-red)"/>
  </svg>
  <p class="date-text">10.08.20</p>
</section>

</body>
</html>
```